Industrial services company requires brochure for new product

We are an industrial services company called Tern Ridge Group. Our clients include major mining, oil and gas and infrastructure clients in Western Australia.

We require a 4 page brochure to feature a new paint removal machine we are bringing to the market in Western Australia.The document will be used predominantly electronically but should be of a quality that can be printed also.

The new machine is an innovative way of removing paint from steel structures as it does not use abrasive blasting to remove the paint. Instead it uses induction heating.

There are some major environmental and safety benefits to using this machine over traditional methods as there are no airborne particles, no noise and minimal waste. The environmental and safety benefits of the are the competitive advantage of the machine and should come through in the marketing.

I have provided as an attachment the proposed copy, the pics available for use, and the Tern Ridge logo.

In general I am thinking page 1 (cover - hero pic/company logo), page 2 (machine information), page 3 (case study) page 4 (about us/contact details/logo etc) but am happy to look at other options.

The images I have attached are the highest quality I will have available.

Target Market(s)

Mining, oil and gas, government infrastructure clients. These are businesses

Industry/Entity Type

Oil And Gas

Requirements
Must have
• The majority of the text supplied as necessary to understand the technology.

```html
<!DOCTYPE html>
<html lang="en">
<head>
<meta charset="utf-8">
<title>Tern Ridge Group – HeatLift Unit Brochure Spread</title>
<link href="https://fonts.googleapis.com/css2?family=Bebas+Neue&family=Open+Sans:wght@400;600;700&display=swap" rel="stylesheet">
<style>
  :root {
    --backdrop: #3a3a3a;
    --paper: #ffffff;
    --paper-fade: #f1f2f3;
    --blue: #1d8fd6;
    --blue-deep: #0e6fb4;
    --navy: #0d4f86;
    --green: #8dc63f;
    --green-deep: #6fae2a;
    --yellow: #fff200;
    --ink: #4a4a4a;
    --ink-dark: #2a2a2a;
  }
  * { box-sizing: border-box; margin: 0; padding: 0; }
  html, body {
    width: 1200px; height: 800px; overflow: hidden;
    background: var(--backdrop);
    font-family: "Open Sans", Arial, sans-serif;
    color: var(--ink);
  }
  .spread {
    position: absolute; left: 168px; top: 97px;
    width: 880px; height: 621px;
  }
  .page {
    position: absolute; top: 0; height: 621px; width: 440px;
    background: var(--paper); overflow: hidden;
  }
  .page--left { left: 0; }
  .page--right { left: 440px; }
  .page-header {
    position: absolute; left: 0; top: 0; width: 440px; height: 79px;
    background: var(--blue);
  }
  .page-title {
    position: absolute; top: 31px;
    font-family: "Bebas Neue", "Oswald", sans-serif; font-weight: 400;
    font-size: 40px; line-height: 40px; color: #fff; letter-spacing: 0.5px;
  }
  .page--left .page-title { left: 45px; }
  .page--right .page-title { right: 42px; }
  .page-footer {
    position: absolute; left: 0; bottom: 0; width: 440px; height: 18px;
    background: var(--paper-fade);
  }
  .body-copy { font-size: 7.2px; line-height: 11px; color: var(--ink); }
  .placeholder { position: absolute; }

  /* Left page */
  .diagram { left: 45px; top: 86px; width: 232px; height: 158px;
    background: linear-gradient(180deg, #ffffff 0%, #eef3f6 55%, #d7dadd 80%, #ffffff 100%); }
  .how-copy { position: absolute; left: 296px; top: 98px; width: 132px; font-size: 7.4px; line-height: 11.2px; }
  .green-band {
    position: absolute; left: 0; top: 263px; width: 414px; height: 32px;
    background: linear-gradient(90deg, var(--green-deep), var(--green));
  }
  .green-band h2 {
    position: absolute; left: 45px; top: 6px;
    font-family: "Bebas Neue", "Oswald", sans-serif; font-weight: 400;
    font-size: 23px; line-height: 23px; color: #fff; white-space: nowrap;
  }
  .safe-copy { position: absolute; left: 45px; top: 314px; width: 232px; }
  .benefits { list-style: none; margin-top: 3px; }
  .benefits li { line-height: 13px; }
  .benefits li::before { content: "• "; }
  .machine { left: 284px; top: 301px; width: 134px; height: 108px;
    background: radial-gradient(ellipse at 55% 50%, #b8bcc0 0%, #8d9297 45%, #ffffff 75%); }
  .asset-copy { position: absolute; left: 45px; top: 421px; width: 375px; }
  .available {
    position: absolute; left: 45px; top: 460px;
    font-family: "Bebas Neue", "Oswald", sans-serif; font-weight: 400;
    font-size: 14px; line-height: 15px; color: var(--blue);
  }
  .sectors { position: absolute; left: 175px; top: 459px; display: flex; gap: 7px; list-style: none; }
  .sector { width: 31px; text-align: center; font-size: 3.4px; line-height: 4px; color: var(--ink-dark); }
  .sector svg { display: block; width: 31px; height: 31px; margin-bottom: 2px; }
  .about-copy { position: absolute; left: 45px; top: 505px; width: 370px; }
  .cta {
    position: absolute; left: 45px; top: 580px;
    font-size: 9.2px; font-weight: 600; color: var(--ink-dark);
  }

  /* Right page */
  .page--right .page-header { background: linear-gradient(90deg, var(--blue-deep), var(--blue)); }
  .hero { left: 0; top: 79px; width: 440px; height: 230px;
    background: linear-gradient(180deg, #2b3d52 0%, #3e5362 30%, #1f4d57 55%, #123a3f 80%, #7a5440 100%); }
  .case-title {
    position: absolute; left: 32px; top: 239px; width: 388px; height: 78px;
    background: var(--blue); padding: 8px 0 0 18px;
    font-family: "Bebas Neue", "Oswald", sans-serif; font-weight: 400;
    font-size: 27.5px; line-height: 31px; color: var(--yellow);
  }
  .case-section { position: absolute; left: 30px; width: 292px; }
  .case-section h3 {
    font-family: "Bebas Neue", "Oswald", sans-serif; font-weight: 400;
    font-size: 12px; line-height: 12px; color: var(--blue-deep);
  }
  .case-section p { font-size: 6.8px; line-height: 9.6px; }
  .case-section p + p { margin-top: 9px; }
  .project { top: 326px; }
  .challenge { top: 395px; }
  .outcome { top: 465px; }
  .thumb { left: 330px; width: 90px; height: 61px; }
  .thumb--1 { top: 328px; background: linear-gradient(180deg, #4a3526, #1a1410); }
  .thumb--2 { top: 393px; background: linear-gradient(180deg, #6d4a30, #2a1d14); }
  .thumb--3 { top: 458px; background: linear-gradient(180deg, #1b2a35, #8a5a36); }
  .thumb--4 { top: 524px; background: linear-gradient(180deg, #2d2d2d, #0f0f0f); }
</style>
</head>
<body>
<main class="spread">

  <section class="page page--left">
    <header class="page-header"><h1 class="page-title">How It Works</h1></header>

    <div class="placeholder diagram" role="img" aria-label="Technical diagram: coatings removal by controlled induction heating, showing the induction head lifting the disbonded coating from a pitted steel substrate"></div>
    <p class="body-copy how-copy">The HeatLift Unit removes paint and coatings from steel surfaces by the principle of induction. Heat is generated in the steel substrate and the bonding is broken. The coating is removed entirely without disintegrating and completely free from contaminating agents like blast media. Even inside the pittings and cracks in the surface the coating is disbonded.</p>

    <div class="green-band"><h2>A Safe, Environmentally Friendly Alternative</h2></div>

    <div class="body-copy safe-copy">
      <p>The HeatLift Unit is especially effective in removing asbestos, lead, coal tar and other toxic coatings without compromising the health of the operators or the environment. The benefits include:</p>
      <ul class="benefits">
        <li>No air borne particles or dust</li>
        <li>No noise – the machine is virtually silent</li>
        <li>No contaminated water waste or wash off</li>
        <li>No contaminated blast media</li>
      </ul>
    </div>
    <div class="placeholder machine" role="img" aria-label="Photo of the stainless steel HeatLift Unit on wheels with its coiled induction head cable"></div>
    <p class="body-copy asset-copy">Asset owners value the opportunity to remove toxic paint and coatings without the contamination risks. No other system does this so quickly, cleanly and effortlessly.</p>

    <h2 class="available">Available for your<br>next maintenance project</h2>
    <ul class="sectors">
      <li class="sector"><svg viewBox="0 0 31 31"><circle cx="15.5" cy="15.5" r="15" fill="#0d6fa8"/><path d="M8 17h15l-3 5H11z M12 11h7v5h-7z" fill="#fff"/></svg>Shipbuilding</li>
      <li class="sector"><svg viewBox="0 0 31 31"><circle cx="15.5" cy="15.5" r="15" fill="#0d6fa8"/><rect x="9" y="10" width="13" height="12" fill="#fff"/><rect x="9" y="10" width="13" height="2" fill="#0d6fa8" opacity=".4"/></svg>Storage Tanks</li>
      <li class="sector"><svg viewBox="0 0 31 31"><circle cx="15.5" cy="15.5" r="15" fill="#0d6fa8"/><rect x="7" y="12" width="17" height="7" rx="3.5" fill="#fff"/></svg>Pipes</li>
      <li class="sector"><svg viewBox="0 0 31 31"><circle cx="15.5" cy="15.5" r="15" fill="#0d6fa8"/><path d="M7 19h17M10 19V10M21 19V10M10 11l5 6 6-6" stroke="#fff" stroke-width="1.6" fill="none"/></svg>Bridges</li>
      <li class="sector"><svg viewBox="0 0 31 31"><circle cx="15.5" cy="15.5" r="15" fill="#0d6fa8"/><path d="M9 22V15h13v7M12 15V9h2v6M8 15h15" stroke="#fff" stroke-width="1.6" fill="none"/></svg>Offshore</li>
      <li class="sector"><svg viewBox="0 0 31 31"><circle cx="15.5" cy="15.5" r="15" fill="#3aa935"/><path d="M10 21c0-7 5-11 12-11-1 7-5 11-12 11z" fill="#fff"/></svg>Health Safety &amp; Environment</li>
    </ul>

    <div class="body-copy about-copy">
      <p>Maintenance services provider Tern Ridge Group Pty Ltd has invested in this globally patented, proven technology from Norwegian manufacturer Norvik Thermal A/S to provide its clients in Western Australia with access to an alternative paint and coatings removal method.</p>
      <p>The HeatLift Unit is a plug and play unit that is easy to mobilise and install anywhere. Tern Ridge Group personnel have achieved their Verification of Competency (VOC) for operation of the HeatLift Unit and have demonstrated experience using the machine on maintenance projects.</p>
    </div>
    <p class="cta">Why not ask us for a quote on your next maintenance project?</p>

    <div class="page-footer"></div>
  </section>

  <section class="page page--right">
    <header class="page-header"><h1 class="page-title">Case Study</h1></header>

    <div class="placeholder hero" role="img" aria-label="Photo of the underside of a wharf over dark green water, with a utility vehicle on the deck and rocks in the foreground"></div>
    <h2 class="case-title">Providing a complete solution at the<br>Coastal Ports Authority</h2>

    <article class="case-section project">
      <h3>The Project</h3>
      <p>The Coastal Ports Authority contracted Tern Ridge Group to lead and manage the Berth 3 Wharf Refurbishment Project at the Port of Port Kestrel. The project requires the removal of the old coal-tar epoxy coating from 2,500 square metres of the underside of the wharf, the repair of the main structural supports and the recoating of the area. The project commenced in early 2014 and will be completed in Q3 2015.</p>
    </article>
    <article class="case-section challenge">
      <h3>The Challenge</h3>
      <p>Managing operator exposure to the hazardous coal tar epoxy being removed and minimising the environmental impacts were critical challenges for the Tern Ridge Group team to overcome. In addition, Berth 3 is the main petrol and diesel fuel terminal at the port and is also utilised for bulk exports, so it was necessary to ensure there was no interruption to wharf operations.</p>
    </article>
    <article class="case-section outcome">
      <h3>The Outcome</h3>
      <p>The HeatLift Unit system was initially tested by Tern Ridge Group and proven to be the safest, cleanest and least disruptive method for the removal of the coal tar epoxy. Following testing, the system was mobilised to the work front utilised on approximately 2,500 square metres of structural steel including the top metre of 60 piles in phase 1 of the project. The rate of removal achieved under the difficult circumstances was 3 square metres per hour. The toxic coatings could then be easily collected, removed and disposed of in line with environmental regulations. To complete the phase 1 remediation works the Tern Ridge team then sandblasted the structural steel and sections of the piles and applied 2 coats of high build high solids epoxy coating.</p>
      <p>In summary, the HeatLift Unit system ensured working with old hazardous creosote coatings was made much safer, quicker and manageable in the conditions prevailing under the wharf.</p>
    </article>

    <div class="placeholder thumb thumb--1" role="img" aria-label="Photo of steel beams under the wharf deck"></div>
    <div class="placeholder thumb thumb--2" role="img" aria-label="Photo of a long enclosed work area beneath the wharf"></div>
    <div class="placeholder thumb thumb--3" role="img" aria-label="Photo of scaffolding around wharf piles above the water"></div>
    <div class="placeholder thumb thumb--4" role="img" aria-label="Photo of dark wharf structure seen from below"></div>

    <div class="page-footer"></div>
  </section>

</main>
</body>
</html>
```